Mosvane Design

Looking for Mosvane banner and square design:
Mosvane Banner
W:1600 px H:400 px
Square
120x120

Logo attached.

Description: Data-Driven stock market portfolio management using quantitative analysis.

```html
<!DOCTYPE html>
<html lang="en">
<head>
<meta charset="utf-8">
<title>Mosvane Banner and Square</title>
<link href="https://fonts.googleapis.com/css2?family=Roboto+Condensed:wght@700&family=Roboto:wght@700&family=Open+Sans:wght@400&family=Montserrat:wght@600&display=swap" rel="stylesheet">
<style>
  :root {
    --page: #e4e5e7;
    --paper: #ffffff;
    --brand-blue: #0b78bd;
    --deep-blue: #1b5c8c;
    --logo-navy: #1f4f7a;
    --ink: #454545;
    --mist: #eff0f1;
    --chart-faint: #ececec;
    --art-light: #bfe3f7;
    --art-mid: #5bb4e8;
  }
  * { margin: 0; padding: 0; box-sizing: border-box; }
  html, body { width: 1200px; height: 568px; overflow: hidden; }
  body { background: var(--page); position: relative; }

  .banner {
    position: absolute; left: 62px; top: 140px;
    width: 1076px; height: 269px;
    background: var(--paper); overflow: hidden;
  }
  .banner-backdrop { position: absolute; inset: 0; }

  .speed-bars { position: absolute; left: 0; top: 0; }
  .speed-bar {
    position: absolute; left: 0; height: 17px;
    background: var(--brand-blue); border-radius: 0 9px 9px 0;
  }

  .headline { position: absolute; left: 87px; top: 72px; }
  .headline-kicker {
    font-family: "Roboto Condensed", sans-serif; font-weight: 700;
    font-size: 27px; line-height: 28px; color: var(--deep-blue);
  }
  .headline-main {
    font-family: "Roboto", sans-serif; font-weight: 700;
    font-size: 40px; line-height: 44px; color: var(--brand-blue);
    letter-spacing: 0.3px; margin-top: 6px;
  }
  .headline-sub {
    font-family: "Open Sans", sans-serif; font-weight: 400;
    font-size: 18.5px; line-height: 23px; color: var(--ink);
    margin-top: 6px;
  }

  .brand-lockup {
    position: absolute; left: 418px; top: 112px;
    display: flex; align-items: center; gap: 14px;
  }
  .brand-dot { width: 40px; height: 40px; border-radius: 50%; background: var(--brand-blue); }
  .brand-name {
    font-family: "Montserrat", sans-serif; font-weight: 600;
    font-size: 30px; color: var(--logo-navy); letter-spacing: 1px;
  }

  .hero-art {
    position: absolute; left: 692px; top: 8px; width: 272px; height: 244px;
    border-radius: 10px;
    background: linear-gradient(150deg, var(--art-light), var(--art-mid));
    opacity: 0.85;
  }

  .square-mark {
    position: absolute; left: 570px; top: 368px; width: 82px; height: 82px;
    background: var(--brand-blue); border: 3px solid var(--paper);
    display: flex; align-items: center; justify-content: center;
  }
  .square-name {
    font-family: "Montserrat", sans-serif; font-weight: 600;
    font-size: 13px; color: var(--paper); letter-spacing: 0.5px;
  }
</style>
</head>
<body>
  <section class="banner">
    <svg class="banner-backdrop" width="1076" height="269" viewBox="0 0 1076 269">
      <g class="market-bars" fill="var(--chart-faint)">
        <rect x="70" y="130" width="14" height="60"/>
        <rect x="140" y="90" width="14" height="80"/>
        <rect x="210" y="110" width="14" height="70"/>
        <rect x="280" y="60" width="14" height="55"/>
        <rect x="330" y="40" width="14" height="70"/>
        <rect x="380" y="35" width="14" height="40"/>
        <rect x="440" y="50" width="14" height="60"/>
        <rect x="500" y="75" width="14" height="90"/>
        <rect x="560" y="100" width="14" height="110"/>
        <rect x="620" y="80" width="14" height="70"/>
        <rect x="660" y="45" width="14" height="60"/>
      </g>
      <path class="market-line" d="M48 126 C120 80 200 30 300 26 C390 22 440 90 520 106 C600 122 640 60 700 16"
            fill="none" stroke="#dcdcdc" stroke-width="1.2"/>
      <g fill="#e0e0e0">
        <circle cx="199" cy="50" r="5"/><circle cx="253" cy="31" r="5"/>
        <circle cx="309" cy="26" r="5"/><circle cx="363" cy="40" r="5"/>
        <circle cx="413" cy="66" r="5"/><circle cx="464" cy="92" r="5"/>
        <circle cx="519" cy="106" r="5"/><circle cx="573" cy="96" r="5"/>
        <circle cx="615" cy="57" r="5"/><circle cx="658" cy="19" r="5"/>
      </g>
      <rect x="950" y="0" width="126" height="269" fill="var(--brand-blue)"/>
      <ellipse cx="800" cy="134" rx="258" ry="300" fill="var(--paper)"/>
      <ellipse cx="800" cy="134" rx="246" ry="294" fill="var(--mist)"/>
    </svg>

    <div class="speed-bars">
      <span class="speed-bar" style="top:55px;width:24px"></span>
      <span class="speed-bar" style="top:91px;width:73px"></span>
      <span class="speed-bar" style="top:126px;width:50px"></span>
      <span class="speed-bar" style="top:161px;width:71px"></span>
      <span class="speed-bar" style="top:196px;width:24px"></span>
    </div>

    <div class="headline">
      <p class="headline-kicker">DATA-DRIVEN</p>
      <h1 class="headline-main">STOCK MARKET</h1>
      <p class="headline-sub">Portfolio Management Using<br>Quantitative Analysis.</p>
    </div>

    <div class="brand-lockup">
      <span class="brand-dot"></span>
      <span class="brand-name">MOSVANE</span>
    </div>

    <div class="hero-art" role="img" aria-label="Isometric illustration of an analyst beside a large monitor with dashboards, bar charts, a plant, cash stacks, coins and a magnifying glass"></div>
  </section>

  <div class="square-mark">
    <span class="square-name">MOSVANE</span>
  </div>
</body>
</html>
```